Thistlewood Joinery Website

My client Thistlewood Joinery is looking for a redesign for a Word Press Website. Their current site is at www.thistlewoodjoinery.example They are a custom cabinet company, but also create bathroom, living room, bar and entertainment and bedroom cabinets too. They would like a design that emulates the master craftsman work they do yet a contemporary style.

Their current site was designed using Flash elements.

Target Market(s)

Home owners and builders of high end homes

Industry/Entity Type

Entertainment

Font styles to use
Serif
Decorative

Requirements
Must have
• Must show their work and logo using a contemporary style.
Nice to have
• Sliders that showcase their projects.

```html
<!DOCTYPE html>
<html lang="en">
<head>
<meta charset="utf-8">
<title>Thistlewood Joinery</title>
<link rel="stylesheet" href="https://fonts.googleapis.com/css2?family=Open+Sans:ital,wght@0,400;0,600;0,700;1,400&family=Oswald:wght@400;500;700&display=swap">
<style>
:root{
  --green:#3bb54a;
  --green-dark:#2c8f38;
  --wood:#7a3f22;
  --wood-dark:#5a2b14;
  --wood-light:#9a5630;
  --brown-btn:#6b2d17;
  --ink:#222;
  --muted:#777;
  --grey-band:#dcdcdc;
  --red-line:#a3161a;
  --footer-bar:#1b1b1b;
  --disc:#bdbdbd;
}
*{box-sizing:border-box;margin:0;padding:0}
html,body{width:1200px;height:2419px;overflow:hidden;background:#fff}
body{position:relative;font-family:"Open Sans",Arial,sans-serif;color:var(--ink)}
.abs{position:absolute}

/* header */
.top-line{left:0;top:0;width:1200px;height:4px;background:var(--red-line)}
.logo{left:152px;top:12px;width:100px;height:100px;border-radius:50%;border:4px solid var(--green-dark);background:#fff;display:flex;align-items:center;justify-content:center;text-align:center;font-size:12px;font-weight:700;color:var(--green-dark);line-height:1.2}
.search{left:810px;top:19px;width:202px;height:30px;border:1px solid #bbb;background:#fff;font-size:12px;color:#999;padding:6px 10px}
.search-btn{left:982px;top:19px;width:30px;height:30px;background:var(--brown-btn)}
.social-btn{left:733px;top:63px;width:76px;height:46px;background:#3b5b99;color:#fff;font-size:12px;font-weight:600;line-height:1.2;padding:7px 8px}
.question{left:890px;top:62px;font-size:12px;color:#333}
.phone{left:890px;top:76px;font-family:"Oswald",sans-serif;font-size:31px;font-weight:700;color:var(--green);letter-spacing:1px}

.hero-band{left:0;top:121px;width:1200px;height:416px;background:linear-gradient(90deg,#b7ac98,#d4cbb9 40%,#c9bfa9 70%,#b3a690)}
.nav{left:162px;top:145px;width:878px;height:49px;background:#efeae2;display:flex;align-items:center;border-bottom:2px solid #d7cfc2}
.nav .home,.nav .srch{flex:none;width:46px;height:49px;background:var(--brown-btn);display:flex;align-items:center;justify-content:center}
.nav a{font-size:11px;font-weight:600;color:#333;text-decoration:none;padding:0 10px;border-right:1px solid #ccc;text-transform:uppercase;white-space:nowrap;line-height:20px}
.nav a:last-of-type{border-right:none}
.nav .srch{margin-left:auto}
.slide{left:162px;top:194px;width:878px;height:406px;background:linear-gradient(180deg,#6b3a1f 0%,#a36a3c 40%,#c9b49a 58%,#8a4a24 75%,#6a3418 100%)}
.slide-title{left:162px;top:452px;width:878px;text-align:center;font-family:"Oswald",sans-serif;font-size:40px;font-weight:700;color:#fff;text-shadow:0 2px 4px rgba(0,0,0,.6)}
.slide-sub{left:162px;top:508px;width:878px;text-align:center;font-size:19px;color:#fff}
.arrow{width:46px;height:46px;border-radius:50%;background:rgba(0,0,0,.35);border:2px solid rgba(255,255,255,.6);display:flex;align-items:center;justify-content:center}
.dots{left:546px;top:556px;display:flex;gap:6px}
.dots span{width:14px;height:14px;border-radius:50%;background:#fff;opacity:.85}

.tagline{left:0;top:640px;width:1200px;text-align:center;font-size:28px;line-height:1.35;color:#333}
.tagline em{font-style:normal;color:var(--green)}

/* offer */
.offer{left:0;top:750px;width:1200px;height:416px;background:linear-gradient(90deg,var(--wood-dark),var(--wood) 30%,var(--wood-light) 55%,var(--wood) 80%,var(--wood-dark))}
.offer-tab{left:436px;top:750px;width:329px;height:40px;background:var(--green);clip-path:polygon(0 0,100% 0,94% 100%,6% 100%);color:#fff;font-size:20px;text-align:center;line-height:40px;letter-spacing:1px}
.service{width:150px;text-align:center;color:#fff;font-size:13px;font-weight:600;text-transform:uppercase}
.service .disc{width:120px;height:120px;margin:0 auto 18px;border-radius:50%;background:radial-gradient(circle,#e2e2e2,#a5a5a5);border:4px solid #eee;display:flex;align-items:center;justify-content:center}
.service.active .disc{background:#222}
.offer-text{left:160px;top:1026px;width:880px;text-align:center;color:#f3e6dc;font-size:13px;line-height:1.6}

/* gallery & news */
.sec-title{font-size:22px;font-weight:400;color:#222;letter-spacing:.5px}
.sec-title span{color:var(--green)}
.thumb{width:194px;height:103px}
.zoom{left:240px;top:1290px;width:36px;height:36px;border-radius:50%;background:var(--green);display:flex;align-items:center;justify-content:center}
.btn-dark{background:#222;color:#fff;font-size:12px;text-align:center;line-height:32px}
.news{left:787px;width:253px;display:flex;gap:10px}
.news .pic{flex:none;width:55px;height:44px;background:linear-gradient(#8a5a3a,#d3c6b3)}
.news b{display:block;font-size:12px;font-weight:600;color:var(--green)}
.news p{font-size:11px;color:#777;line-height:1.3}
.btn-green{background:var(--green);color:#fff;font-size:12px;text-align:center;line-height:32px}
.divider{left:160px;top:1568px;width:880px;height:1px;background:#ddd}

.client{font-size:28px;font-weight:700;color:#111;white-space:nowrap;line-height:1}
.avatar{left:629px;top:1650px;width:70px;height:63px;background:linear-gradient(#6b4a3a,#c9a48a)}
.quote{left:716px;top:1650px;width:324px;height:124px;background:var(--green);border:3px solid var(--green-dark);border-radius:4px;padding:10px 14px;color:#fff;font-size:11.5px;font-style:italic;line-height:1.45;text-align:center}
.quote-by{left:732px;top:1785px;font-size:13px;font-style:italic;color:#555}

.hello{left:0;top:1839px;width:1200px;height:257px;background:var(--grey-band)}
.hello h2{position:absolute;left:0;top:55px;width:1200px;text-align:center;font-family:"Oswald",sans-serif;font-size:36px;color:#222}
.hello p{position:absolute;left:160px;top:112px;width:880px;text-align:center;font-size:13px;color:#777;line-height:1.6}
.share{top:1998px;width:40px;height:40px;border-radius:50%;display:flex;align-items:center;justify-content:center}

.footer{left:0;top:2096px;width:1200px;height:288px;background:linear-gradient(90deg,var(--wood-dark),var(--wood) 35%,var(--wood-light) 60%,var(--wood-dark))}
.f-title{font-size:16px;color:#fff;text-transform:uppercase;letter-spacing:.5px}
.f-text{font-size:12.5px;color:#f2e5db;line-height:1.6}
.pf{width:44px;height:44px;background:linear-gradient(#3a2416,#b8a489);border:1px solid #fff}
.bottom{left:0;top:2384px;width:1200px;height:35px;background:var(--footer-bar);color:#ddd;font-size:12px;line-height:35px}
.bottom .green{color:var(--green)}
</style>
</head>
<body>
<div class="abs top-line"></div>
<div class="abs logo">Thistlewood<br>Joinery</div>
<div class="abs search">enter keyword...</div>
<div class="abs search-btn"></div>
<div class="abs social-btn">Find us on<br>Social</div>
<div class="abs question">Have a Question for Us?</div>
<div class="abs phone">555 010 4826</div>

<div class="abs hero-band" role="img" aria-label="Light wood grain background"></div>
<nav class="abs nav">
  <div class="home"><svg width="18" height="16" viewBox="0 0 18 16"><path d="M9 1L1 8h2v7h4v-5h4v5h4V8h2z" fill="#fff"/></svg></div>
  <a>Who we are</a><a>Getting started</a><a>Contact us</a><a>Customer experience</a><a>Professional</a><a>Portfolio</a><a>Cabinet hardware</a>
  <div class="srch"><svg width="18" height="18" viewBox="0 0 18 18"><circle cx="7" cy="7" r="5" fill="none" stroke="#fff" stroke-width="2"/><path d="M11 11l5 5" stroke="#fff" stroke-width="2.5"/></svg></div>
</nav>
<div class="abs slide" role="img" aria-label="Photo of a kitchen with wooden cabinets and stone counters"></div>
<div class="abs slide-title">AFFORDABLE SOLUTIONS FOR LIVING</div>
<div class="abs slide-sub">Style, Comfort, Quality, Selection!</div>
<div class="abs arrow" style="left:172px;top:385px"><svg width="14" height="18" viewBox="0 0 14 18"><path d="M11 2L3 9l8 7" fill="none" stroke="#fff" stroke-width="3"/></svg></div>
<div class="abs arrow" style="left:982px;top:385px"><svg width="14" height="18" viewBox="0 0 14 18"><path d="M3 2l8 7-8 7" fill="none" stroke="#fff" stroke-width="3"/></svg></div>
<div class="abs dots"><span></span><span></span><span></span><span></span><span></span></div>

<p class="abs tagline">We've been <em>designing and manufacturing</em><br>the Midwest's finest <em>custom cabinets and fixtures</em> since <em>1966</em></p>

<section class="abs offer" role="img" aria-label="Dark wood grain background"></section>
<div class="abs offer-tab">WHAT WE OFFER</div>

<div class="abs service" style="left:143px;top:847px"><div class="disc">
  <svg width="64" height="64" viewBox="0 0 64 64" fill="#222"><circle cx="32" cy="32" r="17"/><circle cx="32" cy="32" r="12" fill="#cfcfcf"/><rect x="6" y="12" width="3" height="40" rx="1.5"/><rect x="3" y="12" width="2" height="12"/><rect x="10" y="12" width="2" height="12"/><path d="M55 12c4 4 4 14 0 18v22h-3V12z"/></svg>
</div>Kitchen</div>
<div class="abs service active" style="left:293px;top:847px"><div class="disc">
  <svg width="64" height="64" viewBox="0 0 64 64" fill="#fff"><path d="M8 32h48v4c0 8-6 14-14 14H22C14 50 8 44 8 36z"/><rect x="14" y="50" width="4" height="6"/><rect x="46" y="50" width="4" height="6"/><path d="M14 32V14a5 5 0 0 1 10 0" fill="none" stroke="#fff" stroke-width="3"/><circle cx="30" cy="24" r="2"/><circle cx="36" cy="20" r="2"/><circle cx="40" cy="26" r="2"/></svg>
</div>Bath</div>
<div class="abs service" style="left:443px;top:847px"><div class="disc">
  <svg width="64" height="64" viewBox="0 0 64 64" fill="#222"><rect x="16" y="12" width="32" height="22" rx="2"/><rect x="19" y="15" width="26" height="16" fill="#cfcfcf"/><rect x="29" y="34" width="6" height="6"/><rect x="8" y="40" width="48" height="4"/><rect x="11" y="44" width="4" height="12"/><rect x="49" y="44" width="4" height="12"/></svg>
</div>Office</div>
<div class="abs service" style="left:595px;top:847px"><div class="disc">
  <svg width="64" height="64" viewBox="0 0 64 64" fill="none" stroke="#222" stroke-width="3"><path d="M32 22v-4a4 4 0 1 1 4 -4"/><path d="M32 22L8 40h48z" stroke-linejoin="round"/><rect x="14" y="44" width="36" height="10" fill="#222"/></svg>
</div>Closet</div>
<div class="abs service" style="left:748px;top:847px"><div class="disc">
  <svg width="64" height="64" viewBox="0 0 64 64" fill="#222"><rect x="8" y="26" width="48" height="5" rx="1"/><rect x="12" y="31" width="4" height="22"/><rect x="48" y="31" width="4" height="22"/><rect x="14" y="14" width="18" height="8" rx="1"/><path d="M38 22l6-10 6 10z"/><rect x="12" y="42" width="40" height="3"/></svg>
</div>Workshop</div>
<div class="abs service" style="left:898px;top:847px"><div class="disc">
  <svg width="64" height="64" viewBox="0 0 64 64" fill="#222"><rect x="8" y="12" width="48" height="30" rx="2"/><rect x="11" y="15" width="42" height="24" fill="#cfcfcf"/><rect x="28" y="42" width="8" height="6"/><rect x="12" y="48" width="40" height="5" rx="1"/><path d="M28 21v12l10-6z"/></svg>
</div>Entertainment</div>

<p class="abs offer-text">Sed ut aperiam, eaque ipsa quae ab illo inventore veritatis et quasi architecto beatae vitae dicta sunt explicabo. Nemo sit perspiciatis unde omnis iste natus error sit voluptatem accusantium doloremque laudantium, totam rem aperiam, eaque ipsa quae ab illo inventore veritatis et quasi architecto beatae vitae dicta sunt explicabo. Nemo sit voluptatem doloremque laudantium, nesciunt ae ab illo inventore veritatis et quasi architecto beatae vitae dicta sunt expli.</p>

<h3 class="abs sec-title" style="left:160px;top:1212px">OUR <span>GALLERY</span></h3>
<div class="abs thumb" style="left:160px;top:1256px;background:linear-gradient(160deg,#2f2c29,#5d564d 55%,#8c8478)" role="img" aria-label="Project photo: dark kitchen with island"></div>
<div class="abs zoom"><svg width="18" height="18" viewBox="0 0 18 18"><circle cx="7" cy="7" r="5" fill="none" stroke="#fff" stroke-width="2"/><path d="M11 11l5 5" stroke="#fff" stroke-width="2.5"/></svg></div>
<div class="abs thumb" style="left:363px;top:1256px;background:linear-gradient(180deg,#e4ded4,#b7a58c 55%,#5e4836)" role="img" aria-label="Project photo: bright kitchen with wood cabinets"></div>
<div class="abs thumb" style="left:569px;top:1256px;background:linear-gradient(180deg,#f1eee9,#c9c1b5 55%,#3a302a)" role="img" aria-label="Project photo: white kitchen with dark appliances"></div>
<div class="abs thumb" style="left:160px;top:1370px;background:linear-gradient(180deg,#d6d0c8,#8a7f72 45%,#231e1a)" role="img" aria-label="Project photo: kitchen with dark cabinets"></div>
<div class="abs thumb" style="left:363px;top:1370px;background:linear-gradient(180deg,#ddd7cf,#6c5f52 45%,#1e1a16)" role="img" aria-label="Project photo: dark island with stools"></div>
<div class="abs thumb" style="left:569px;top:1370px;background:linear-gradient(180deg,#d3ccc2,#7d6f60 50%,#2e2520)" role="img" aria-label="Project photo: espresso cabinets with granite counters"></div>
<div class="abs btn-dark" style="left:160px;top:1488px;width:128px;height:32px">VIEW MORE</div>

<h3 class="abs sec-title" style="left:787px;top:1212px">RECENT <span>NEWS</span></h3>
<div class="abs news" style="top:1258px"><div class="pic"></div><div><b>Morbi id malesuada augue elis</b><p>Morbi id malesuada augue, auctor ahlc nunc sit amet, lobortis.</p></div></div>
<div class="abs news" style="top:1343px"><div class="pic"></div><div><b>Morbi id malesuada augue elis</b><p>Morbi id malesuada augue, auctor ahlc nunc sit amet, lobortis.</p></div></div>
<div class="abs news" style="top:1428px"><div class="pic"></div><div><b>Morbi id malesuada augue elis</b><p>Morbi id malesuada augue, auctor ahlc nunc sit amet, lobortis.</p></div></div>
<div class="abs btn-green" style="left:787px;top:1488px;width:132px;height:32px">VIEW MORE</div>

<div class="abs divider"></div>

<h3 class="abs sec-title" style="left:160px;top:1598px">OUR <span>CLIENTS</span></h3>
<div class="abs client" style="left:164px;top:1662px">Verane</div>
<div class="abs client" style="left:307px;top:1662px">La Brisa</div>
<div class="abs client" style="left:484px;top:1662px">Torvan</div>
<div class="abs client" style="left:164px;top:1748px">Kestra</div>
<div class="abs client" style="left:307px;top:1748px">Calvend</div>
<div class="abs client" style="left:466px;top:1748px">Halworth</div>

<h3 class="abs sec-title" style="left:624px;top:1598px">TESTIMONIALS</h3>
<div class="abs avatar" role="img" aria-label="Client portrait photo"></div>
<div class="abs quote">"Lorem ipsum dolor sit amet, consectetur adipiscing elit, sed do eiusmod tempor incididunt ut labore et dolore magna aliqua. Ut enim ad minim veniam, quis nostrud exercitation ullamco laboris nisi ut aliquip ex ea commodo consequat. Duis aute irure dolor in reprehenderit."</div>
<div class="abs quote-by">- Mara Quinn</div>

<section class="abs hello">
  <h2>HELLO !</h2>
  <p>Sed ut perspiciatis unde omnis iste natus error sit voluptatem accusantium doloremque laudantium, totam rem aperiam, eaque ipsa quae e natus error sit voluptab illo inventore veritatis et quasi architecto beatae vitae dicta sunt explicabo.</p>
</section>
<div class="abs share" style="left:513px;background:#2aa3e0"></div>
<div class="abs share" style="left:563px;background:#3b5b99"></div>
<div class="abs share" style="left:613px;background:#d23c2a"></div>
<div class="abs share" style="left:663px;background:#2b8a4a"><svg width="18" height="18" viewBox="0 0 18 18" fill="#fff"><circle cx="4" cy="9" r="2.5"/><circle cx="14" cy="4" r="2.5"/><circle cx="14" cy="14" r="2.5"/><path d="M4 9L14 4M4 9l10 5" stroke="#fff" stroke-width="1.5"/></svg></div>

<footer class="abs footer" role="img" aria-label="Dark wood grain background"></footer>
<h4 class="abs f-title" style="left:160px;top:2138px">About us</h4>
<p class="abs f-text" style="left:160px;top:2168px;width:290px;text-align:justify">Established in 1966, <b>Thistlewood Joinery</b> has long stood as one of the Midwest's most renowned makers of custom cabinets and fixtures. Our handcrafted, award-winning creations have been chosen by hundreds of noteworthy homebuilders. And while we custom build cabinets, we built our business around the belief that our customers absolutely, unequivocally come first.</p>

<h4 class="abs f-title" style="left:508px;top:2138px">Recent portfolio</h4>
<div class="abs" style="left:508px;top:2170px;display:grid;grid-template-columns:repeat(4,44px);gap:6px">
  <div class="pf"></div><div class="pf"></div><div class="pf"></div><div class="pf"></div>
  <div class="pf"></div><div class="pf"></div><div class="pf"></div><div class="pf"></div>
  <div class="pf"></div><div class="pf"></div><div class="pf"></div><div class="pf"></div>
</div>

<h4 class="abs f-title" style="left:787px;top:2138px">Contact us</h4>
<p class="abs f-text" style="left:787px;top:2168px;width:260px;font-size:11.5px;line-height:1.45"><b>Got a question for Thistlewood? We'd love to hear from you! Whether it's for a project inquiry.</b><br><b>Thistlewood Joinery</b><br>Owen Harlow, 4410 Larchmont Road, Fernbrook, MO-60000</p>
<svg class="abs" style="left:787px;top:2264px" width="20" height="90" viewBox="0 0 20 90" fill="#fff">
  <path d="M4 0h4l2 5-3 2c1 3 3 5 6 6l2-3 5 2v4c0 1-1 2-2 2C8 18 0 10 0 2c0-1 1-2 2-2z"/>
  <rect x="1" y="34" width="18" height="13" rx="2"/>
  <path d="M1 68h18v12H1zM1 68l9 7 9-7" fill="none" stroke="#fff" stroke-width="2"/>
</svg>
<p class="abs f-text" style="left:827px;top:2260px;line-height:34px;font-weight:600">555.010.2300<br>555.010.7835<br>bill@thistlewoodjoinery.example</p>

<div class="abs bottom">
  <span style="position:absolute;left:160px"><span class="green">Home</span> | Who Are We | Professional | Portfolio | Contact Us</span>
  <span style="position:absolute;right:160px">© 2015. All rights reserved. <b>Thistlewood Joinery.</b></span>
</div>
</body>
</html>
```